Stationary Design For New Dynamic Company

Hi there we require stationary designed for our new company, we have used "Pixel Harbor" recently for our logo and were very impressed with all of the designers that contributed towards the final result.
What we require now is the following:
Letter head layout (A4)
Business Cards (5 people)
With Compliments slips
Envelopes
Email stationary
We would like to use our current logo design and I have included it for your use (JPEG is the one we have chosen and I have attached an EPS file for your use). Our company specializes in architectural cladding and our products are used by architects, builders and private clients, so we wish for the stationary to be suitable and attractive to our clientele.
I thank everyone in advance for your contributions.
Thank you to all that have provided your designs for this project, I apologize for not providing feedback as I have been away. I have looked at everyone's designs and they all look great and I will come back to those designers that I wish to have changes made sometime today.
Once again a big thank you to all involved.
Business

```html
<!DOCTYPE html>
<html lang="en">
<head>
<meta charset="utf-8">
<title>Strataline Stationery Set</title>
<link rel="stylesheet" href="https://fonts.googleapis.com/css2?family=Didact+Gothic&display=swap">
<style>
  :root {
    --backdrop: #4b4b4b;
    --paper: #ffffff;
    --orange: #f26a21;
    --navy: #1c2358;
    --ink: #4a4a4a;
    --ink-soft: #8a8a8a;
  }
  * { box-sizing: border-box; margin: 0; padding: 0; }
  html, body { width: 1200px; height: 800px; overflow: hidden; }
  body {
    background: var(--backdrop);
    font-family: "Didact Gothic", "Century Gothic", sans-serif;
    color: var(--ink);
    position: relative;
  }
  .piece { position: absolute; }
  .sheet { background: var(--paper); }

  /* brand lockup */
  .brand { position: absolute; display: flex; align-items: center; gap: 6px; color: var(--navy); }
  .brand-mark { width: 12px; height: 12px; background: var(--orange); }
  .brand-name { font-size: 19px; letter-spacing: 0.5px; }
  .brand--light { color: var(--paper); }
  .brand--light .brand-mark { background: var(--paper); }
  .brand--large .brand-mark { width: 16px; height: 16px; }
  .brand--large .brand-name { font-size: 26px; }

  .address { position: absolute; text-align: right; font-size: 8px; line-height: 10px; color: var(--ink); }

  /* compliments slip */
  .slip { left: 16px; top: 16px; width: 588px; height: 240px; }
  .slip .brand { right: 28px; top: 30px; }
  .slip .address { right: 28px; top: 66px; }
  .slip-title {
    position: absolute; right: 22px; bottom: 16px;
    font-size: 46px; letter-spacing: 1px; color: var(--orange); font-weight: 400;
  }

  /* business card front */
  .card-front { left: 16px; top: 396px; width: 344px; height: 216px; }
  .card-front .brand { right: 30px; top: 20px; }
  .card-person { position: absolute; right: 26px; top: 84px; text-align: right; }
  .card-name { font-size: 15px; color: var(--ink); }
  .card-role { font-size: 8px; color: var(--ink-soft); margin-top: 2px; }
  .card-contact { position: absolute; right: 26px; top: 116px; text-align: right; font-size: 10px; line-height: 13px; }
  .card-front .address { right: 26px; top: 168px; font-size: 10px; line-height: 13px; }

  /* business card back */
  .card-back { left: 16px; top: 636px; width: 344px; height: 156px; background: var(--orange); }
  .card-back .brand { left: 150px; top: 62px; }

  /* DL slip */
  .dl { left: 386px; top: 280px; width: 220px; height: 510px; }
  .dl-band { position: absolute; left: 0; top: 0; width: 100%; height: 70px; background: var(--orange); }
  .dl .brand { left: 40px; top: 700px; top: 420px; }
  .dl .address { left: 70px; top: 450px; text-align: left; }

  /* envelope */
  .envelope { left: 632px; top: 370px; width: 428px; height: 420px; background: var(--orange); }
  .envelope .brand { left: 176px; top: 290px; }

  /* letterhead */
  .letter { left: 752px; top: 16px; width: 432px; height: 584px; box-shadow: -2px 2px 6px rgba(0,0,0,0.25); }
  .letter .brand { right: 24px; top: 26px; }
  .letter .address { right: 24px; top: 64px; }
  .letter-body { position: absolute; left: 22px; top: 132px; width: 392px; font-size: 7px; line-height: 9.5px; color: var(--ink); }
  .recipient { margin-bottom: 70px; }
  .subject { font-weight: 700; color: var(--ink); margin-bottom: 14px; letter-spacing: 0.3px; }
  .letter-body p { margin-bottom: 12px; text-align: justify; }
  .signoff { position: absolute; right: 40px; top: 522px; font-size: 7px; color: var(--ink); }
  .signature-line { position: absolute; right: 40px; top: 556px; width: 70px; height: 1px; background: var(--ink-soft); }
</style>
</head>
<body>

  <section class="piece sheet slip">
    <div class="brand"><span class="brand-mark"></span><span class="brand-name">STRATALINE</span></div>
    <div class="address">Suite 4,<br>Larkin Court Arcade<br>12 Fern Street, Geelong</div>
    <h1 class="slip-title">WITH COMPLIMENTS</h1>
  </section>

  <section class="piece sheet card-front">
    <div class="brand"><span class="brand-mark"></span><span class="brand-name">STRATALINE</span></div>
    <div class="card-person">
      <div class="card-name">Mara Quinlan</div>
      <div class="card-role">director</div>
    </div>
    <div class="card-contact">m 0400 555 120<br>mara@strataline.com.au<br>www.strataline.com.au</div>
    <div class="address">Suite 4, Larkin Court Arcade<br>12 Fern Street, Geelong</div>
  </section>

  <section class="piece card-back">
    <div class="brand brand--light"><span class="brand-mark"></span><span class="brand-name">STRATALINE</span></div>
  </section>

  <section class="piece sheet dl">
    <div class="dl-band"></div>
    <div class="brand"><span class="brand-mark"></span><span class="brand-name">STRATALINE</span></div>
    <div class="address">Suite 4,<br>Larkin Court Arcade<br>12 Fern Street, Geelong</div>
  </section>

  <section class="piece envelope">
    <div class="brand brand--light brand--large"><span class="brand-mark"></span><span class="brand-name">STRATALINE</span></div>
  </section>

  <section class="piece sheet letter">
    <div class="brand"><span class="brand-mark"></span><span class="brand-name">STRATALINE</span></div>
    <div class="address">Suite 4,<br>Larkin Court Arcade<br>12 Fern Street, Geelong</div>
    <div class="letter-body">
      <div class="recipient">To,<br>Client Name<br>Street Address</div>
      <div class="subject">Re: cladding supply for the riverside apartment project</div>
      <p>Thank you for meeting with our team last week to review cladding options for the new riverside project. We have attached samples and pricing for the panels discussed, along with installation timelines for each stage of the build. Our project manager will contact you to confirm site access and delivery dates.</p>
      <p>All panels are made to order in our Geelong workshop and finished with a durable coating suited to coastal conditions. Each order is checked against the architect's drawings before dispatch, and our installers work closely with builders on site to keep the program on track. We offer a range of profiles, colours and fixing systems, so the facade can match the design intent without adding cost or delay. Should you need further detail on fire ratings, thermal performance or warranty terms, our technical staff are happy to meet with you or your consultants. We look forward to working with you on this project and to building a lasting relationship with your team.</p>
    </div>
    <div class="signoff">Yours faithfully</div>
    <div class="signature-line"></div>
  </section>

</body>
</html>
```